Ombrik Partnering Business Card

Hello everyone. We need a business card design that would match our logo and the theme we're trying to have for Ombrik that you can find on our website and/or Linkedin page

```html
<!DOCTYPE html>
<html lang="en">
<head>
<meta charset="utf-8">
<title>Ombrik Partnering Business Card</title>
<link href="https://fonts.googleapis.com/css2?family=Jost:wght@400;500;600&display=swap" rel="stylesheet">
<style>
  :root {
    --page-bg: #e6e5ea;
    --card-white: #ffffff;
    --brand-purple: #2d1a55;
    --brand-purple-deep: #241546;
    --ink-light: #d9d7de;
    --muted: #4a3b6e;
  }
  * { margin: 0; padding: 0; box-sizing: border-box; }
  html, body {
    width: 1200px; height: 900px; overflow: hidden;
    background: var(--page-bg);
    font-family: "Jost", Arial, sans-serif;
  }
  .sheet {
    width: 1200px; height: 900px;
    display: flex; flex-direction: column;
    align-items: center; justify-content: center; gap: 56px;
  }
  .card {
    position: relative;
    width: 540px; height: 308px;
    border-radius: 16px;
    box-shadow: 0 10px 28px rgba(30, 20, 60, 0.18);
  }
  .card--front { background: var(--card-white); color: var(--brand-purple); }
  .card--back {
    background: linear-gradient(160deg, var(--brand-purple) 0%, var(--brand-purple-deep) 100%);
    color: var(--ink-light);
    display: flex; flex-direction: column; align-items: center; justify-content: center; gap: 26px;
  }
  .holder { position: absolute; left: 40px; top: 36px; }
  .holder__name { font-size: 21px; font-weight: 600; letter-spacing: 0.5px; text-transform: uppercase; line-height: 1.1; }
  .holder__role { font-size: 13px; font-weight: 400; color: var(--muted); margin-top: 2px; }
  .contacts { position: absolute; left: 40px; bottom: 40px; list-style: none; }
  .contacts li { display: flex; align-items: center; gap: 9px; font-size: 13.5px; line-height: 22px; }
  .contacts svg { width: 11px; height: 11px; flex: none; }
  .brand {
    display: flex; align-items: center; gap: 8px;
    font-weight: 600; white-space: nowrap;
  }
  .brand__dot { border-radius: 50%; flex: none; }
  .card--front .brand { position: absolute; right: 40px; top: 118px; font-size: 19px; color: var(--brand-purple); }
  .card--front .brand__dot { width: 12px; height: 12px; background: var(--brand-purple); }
  .card--back .brand { font-size: 36px; color: var(--ink-light); }
  .card--back .brand__dot { width: 20px; height: 20px; background: var(--ink-light); }
  .address {
    position: absolute; right: 40px; bottom: 36px;
    font-size: 14px; line-height: 19px; text-align: right; font-style: normal;
  }
  .back__web { font-size: 15px; letter-spacing: 0.3px; }
</style>
</head>
<body>
<main class="sheet">
  <section class="card card--front" aria-label="Card front">
    <div class="holder">
      <h1 class="holder__name">Daniel Reyes</h1>
      <p class="holder__role">Founder</p>
    </div>
    <ul class="contacts">
      <li>
        <svg viewBox="0 0 12 12" aria-hidden="true"><path d="M2.5 1h2l1 2.5-1.3 1a6 6 0 0 0 3.3 3.3l1-1.3 2.5 1v2a1 1 0 0 1-1 1A9 9 0 0 1 1.5 2a1 1 0 0 1 1-1z" fill="currentColor"/></svg>
        555-014-2290
      </li>
      <li>
        <svg viewBox="0 0 12 12" aria-hidden="true"><rect x="1" y="2.5" width="10" height="7" rx="1" fill="none" stroke="currentColor" stroke-width="1.2"/><path d="M1.5 3l4.5 3.5L10.5 3" fill="none" stroke="currentColor" stroke-width="1.2"/></svg>
        info@ombrikpartnering.com
      </li>
      <li>
        <svg viewBox="0 0 12 12" aria-hidden="true"><circle cx="6" cy="6" r="5" fill="none" stroke="currentColor" stroke-width="1.1"/><ellipse cx="6" cy="6" rx="2.2" ry="5" fill="none" stroke="currentColor" stroke-width="1"/><path d="M1 6h10" stroke="currentColor" stroke-width="1"/></svg>
        www.ombrikpartnering.com
      </li>
    </ul>
    <div class="brand"><span class="brand__dot"></span>Ombrik Partnering</div>
    <address class="address">480 Harbor Line Rd.<br>Coral Shore,<br>FL 30000</address>
  </section>

  <section class="card card--back" aria-label="Card back">
    <div class="brand"><span class="brand__dot"></span>Ombrik Partnering</div>
    <p class="back__web">www.ombrikpartnering.com</p>
  </section>
</main>
</body>
</html>
```